Home inspection business! professional look attracting customers just by looks. Read must haves

its a new business I started on my own for home inspections I would like something very professional to give to real estate agents and clients, its going to have my license number on it my business phone number my name my website as well etc on the back side it will be servicing areas and also what kind of services I offer I also have a business card from someone else the way I would like mine to be. I will attach my logo

Industry/Entity Type

Home Inspection

Contact Information for Business Card

listed in nice to haves

Requirements
Must have
• phone number - 718 352 9047
• website- crestwoodlatch.example
• license number #2749035186
• my name Gavin teraskovic
• picture of my logo and me on the front
• on the back of the card. stating I am servicing All of New York and Long Island
• also services I will offer will be home inspection -mold inspection -lead inspection -radon inspection -Termite Inspection -Infared Scan.
• and also we provide inspections for single family homes condos co-ops town-homes
• and commercial property
Nice to have
• same colors as the logos and also if you recommend fonts to look like the logo not sure up to you

```html
<!DOCTYPE html>
<html lang="en">
<head>
<meta charset="utf-8">
<title>Crestwood Latch Home Inspectors – Business Card</title>
<link rel="stylesheet" href="https://fonts.googleapis.com/css2?family=Montserrat:wght@600;700&family=Questrial&display=swap">
<style>
  :root {
    --backdrop: #e9e9ea;
    --card: #333335;
    --card-edge: #3d8fd8;
    --accent: #3d8fd8;
    --ink: #f2f2f2;
    --ink-soft: #d4d4d6;
    --rule: #cfcfd2;
  }
  * { box-sizing: border-box; margin: 0; padding: 0; }
  html, body {
    width: 1200px; height: 801px; overflow: hidden;
    background: var(--backdrop);
  }
  .canvas {
    position: relative; width: 1200px; height: 801px;
    display: flex; align-items: center; justify-content: space-between;
    padding: 0 40px;
  }
  .card {
    position: relative; width: 540px; height: 309px;
    background: var(--card);
    border-bottom: 4px solid var(--card-edge);
    border-left: 4px solid var(--card-edge);
    color: var(--ink);
    font-family: "Questrial", sans-serif;
    box-shadow: 0 10px 24px rgba(0,0,0,.18);
  }
  .brand {
    position: absolute; display: flex; align-items: center; gap: 10px;
    font-family: "Montserrat", sans-serif; font-weight: 700; color: var(--ink);
  }
  .brand-dot { width: 14px; height: 14px; border-radius: 50%; background: var(--accent); flex: none; }
  .brand-name { font-size: 22px; line-height: 1.05; letter-spacing: .5px; text-transform: uppercase; }
  .brand-name small { display: block; font-size: 11px; letter-spacing: 5px; }

  /* front */
  .card-front .brand { top: 38px; right: 34px; }
  .card-front .header-rule {
    position: absolute; top: 112px; left: 250px; right: 34px;
    height: 1px; background: var(--rule);
  }
  .holder-name {
    position: absolute; left: 36px; top: 168px;
    font-family: "Montserrat", sans-serif; font-weight: 600;
    font-size: 20px; color: var(--accent); letter-spacing: .5px;
    text-transform: uppercase;
  }
  .name-rule {
    position: absolute; left: 36px; top: 200px; width: 220px;
    height: 1px; background: var(--rule);
  }
  .contact-list { position: absolute; left: 36px; top: 212px; list-style: none; }
  .contact-list li {
    display: flex; align-items: center; gap: 10px;
    font-size: 15px; line-height: 24px; color: var(--ink-soft);
  }
  .contact-list svg { width: 13px; height: 13px; flex: none; }
  .contact-list .link { color: var(--accent); }
  .license {
    position: absolute; right: 34px; bottom: 80px;
    font-size: 14px; color: var(--ink-soft);
  }

  /* back */
  .card-back .brand { top: 40px; right: 30px; }
  .services-title {
    position: absolute; right: 30px; top: 120px;
    font-family: "Montserrat", sans-serif; font-weight: 700;
    font-size: 24px; color: var(--accent); letter-spacing: .5px;
  }
  .coverage {
    position: absolute; left: 30px; right: 30px; top: 166px;
    font-size: 13px; line-height: 20px; color: var(--ink-soft);
  }
  .coverage strong { color: var(--accent); font-weight: 400; }
  .services-list {
    position: absolute; left: 30px; right: 24px; bottom: 24px;
    display: flex; flex-wrap: wrap; list-style: none; row-gap: 6px;
  }
  .services-list li {
    font-size: 15px; color: var(--ink-soft); margin-right: 12px; white-space: nowrap;
  }
  .services-list li::before { content: "• "; color: var(--accent); }
</style>
</head>
<body>
<main class="canvas">

  <section class="card card-front" aria-label="Card front">
    <div class="brand">
      <span class="brand-dot"></span>
      <span class="brand-name">Crestwood Latch<small>Home Inspectors</small></span>
    </div>
    <div class="header-rule"></div>

    <h1 class="holder-name">Gavin Teraskovic</h1>
    <div class="name-rule"></div>
    <ul class="contact-list">
      <li>
        <svg viewBox="0 0 16 16" fill="var(--ink-soft)" aria-hidden="true"><path d="M3.6 1.5l2.2 2.6-1.3 1.6c.9 2 2.3 3.4 4.3 4.3l1.6-1.3 2.6 2.2-1.2 2.4C6.7 13 3 9.3 1.2 2.7z"/></svg>
        718 352 9047
      </li>
      <li>
        <svg viewBox="0 0 16 16" fill="none" stroke="var(--ink-soft)" stroke-width="1.5" aria-hidden="true"><rect x="1.5" y="3.5" width="13" height="9"/><path d="M1.5 3.5l6.5 5 6.5-5"/></svg>
        info@crestwoodlatch.example
      </li>
      <li>
        <svg viewBox="0 0 16 16" fill="none" stroke="var(--ink-soft)" stroke-width="1.3" aria-hidden="true"><circle cx="8" cy="8" r="6.5"/><ellipse cx="8" cy="8" rx="3" ry="6.5"/><path d="M1.5 8h13M2.5 5h11M2.5 11h11"/></svg>
        <span>www.<span class="link">crestwoodlatch.example</span></span>
      </li>
    </ul>
    <p class="license">license number #2749035186</p>
  </section>

  <section class="card card-back" aria-label="Card back">
    <div class="brand">
      <span class="brand-dot"></span>
      <span class="brand-name">Crestwood Latch<small>Home Inspectors</small></span>
    </div>
    <h2 class="services-title">SERVICES</h2>
    <div class="coverage">
      <p><strong>Servicing</strong> All of New York and Long Island</p>
      <p>Single-Family Homes · Condos · Co-ops · Townhomes · Commercial</p>
    </div>
    <ul class="services-list">
      <li>Home Inspection</li>
      <li>Mold Inspection</li>
      <li>Lead Inspection</li>
      <li>Radon Inspection</li>
      <li>Termite Inspection</li>
      <li>Infared Scan</li>
    </ul>
  </section>

</main>
</body>
</html>
```